Women's Health Company needs business card

We need a business card for a USA based women's health care company. We use digital technology to enhance therapy prescribed by clinicians for their patients

```html
<!DOCTYPE html>
<html lang="en">
<head>
<meta charset="utf-8">
<title>Lunora Health – Business Card</title>
<link rel="stylesheet" href="https://fonts.googleapis.com/css2?family=Source+Sans+3:wght@400;600&display=swap">
<style>
  :root {
    --page-bg: #e4e4e4;
    --brand-purple: #8a5299;
    --brand-teal: #72b8b5;
    --card-white: #f4f4f4;
    --ink: #2a2a2a;
    --on-purple: #ffffff;
  }
  * { margin: 0; padding: 0; box-sizing: border-box; }
  html, body {
    width: 1200px; height: 960px; overflow: hidden;
    background: var(--page-bg);
    font-family: "Source Sans 3", sans-serif;
  }
  .card {
    position: absolute;
    left: 296px;
    width: 609px;
    height: 347px;
    overflow: hidden;
  }
  .card-front {
    top: 112px;
    background: var(--brand-purple);
    display: flex; align-items: center; justify-content: center;
  }
  .front-wordmark {
    color: var(--brand-teal);
    font-size: 60px;
    font-weight: 400;
    letter-spacing: 1px;
  }
  .card-back {
    top: 513px;
    background: var(--card-white);
    color: var(--ink);
  }
  .back-waves { position: absolute; inset: 0; }
  .back-wordmark {
    position: absolute; left: 43px; top: 58px;
    color: var(--brand-teal);
    font-size: 38px; font-weight: 400; line-height: 1;
  }
  .holder {
    position: absolute; right: 37px; top: 64px; text-align: right;
  }
  .holder-name {
    color: var(--brand-teal);
    font-size: 21px; font-weight: 600; line-height: 1.2;
  }
  .holder-role { font-size: 16px; line-height: 1.3; }
  .address {
    position: absolute; left: 43px; top: 184px;
    font-size: 15.5px; line-height: 21px;
  }
  .contacts {
    position: absolute; left: 43px; top: 238px;
    list-style: none; font-size: 15.5px; line-height: 22px;
  }
  .contacts li { display: flex; align-items: center; gap: 5px; }
  .contacts svg { width: 13px; height: 13px; fill: var(--brand-purple); }
  .website {
    position: absolute; right: 26px; top: 302px;
    color: var(--on-purple); font-size: 15.5px;
  }
</style>
</head>
<body>
  <section class="card card-front">
    <span class="front-wordmark">Lunora Health</span>
  </section>

  <section class="card card-back">
    <svg class="back-waves" viewBox="0 0 609 347" aria-hidden="true">
      <path fill="var(--brand-teal)" d="M0,277 C150,318 390,318 545,227 C400,302 200,342 0,316 Z"/>
      <path fill="var(--brand-purple)" d="M0,322 C220,348 460,318 609,183 L609,347 L0,347 Z"/>
    </svg>
    <span class="back-wordmark">Lunora Health</span>
    <div class="holder">
      <p class="holder-name">Daniel Reyes</p>
      <p class="holder-role">Founder</p>
    </div>
    <p class="address">418 Harbor Lane, Suite 120<br>Tampa, Florida, 33602</p>
    <ul class="contacts">
      <li>
        <svg viewBox="0 0 24 24" aria-hidden="true"><path d="M6.6 10.8a15.2 15.2 0 0 0 6.6 6.6l2.2-2.2a1 1 0 0 1 1-.25 11.4 11.4 0 0 0 3.6.57 1 1 0 0 1 1 1V20a1 1 0 0 1-1 1A17 17 0 0 1 3 4a1 1 0 0 1 1-1h3.5a1 1 0 0 1 1 1c0 1.25.2 2.45.57 3.57a1 1 0 0 1-.25 1z"/></svg>
        (555) 014-2290
      </li>
      <li>
        <svg viewBox="0 0 24 24" aria-hidden="true"><path d="M2 5h20v14H2z M4 7v.5l8 5 8-5V7l-8 5z" fill-rule="evenodd"/></svg>
        daniel@lunorahealth.com
      </li>
    </ul>
    <span class="website">www.lunorahealth.com</span>
  </section>
</body>
</html>
```